Public Assistance Direct mail piece

need a full color 2 sided marketing brochure to use in direct mail campaign. finished product will be printed on 2 times. initially full color brochures to be printed in bulk. Then consumer contact info and case manager contact info will be added at a later date.
brochure will need to have 2 blank areas on front side to print address that will show thru window envelope and sales agent info on for mail campaign.
Would like to see designs that include our current color scheme and logo.
Target market. Low income poverty. Non profit service offering free assistance to help low income seniors get free assitance thru state and federal public assistance programs.
1. Sanorel - over 1 in 5 recieve help from state Sanorel. Sanorel programs for seniors and persons on Vitalcor can pay doctor copays, deductibles, and assist with medical bills.
2. Silver Bridge Program - receive Federal assistance with prescription medications, deductibles, copays, and drug plan premiums.
3. Vitalcor Thrift Program - many adults 65 and over are eligible to receive Vitalcor at no cost. The program will pay your Vitalcor Tier K premium and can even refund some previous payments.

You may be eligible to participate in one or more of these programs. All programs are based on limited income and assets.

To learn more call your local county case manager.

Knowledge is Power. Lets up help empower you.
Pay it forward. Who else do you know that is on Vitalcor that could use some help?

many graphs and illustrations are available form each government agency.

Target Market(s)

Seniors 65 plus, Vitalcor recipients

Industry/Entity Type

Marketing

Colors
0355a3
ec1f27
ffffff

Requirements
Must have
• logo, non profit, will need a government disclaimer somewhere
Nice to have
• photos of seniors saving money.

```html
<!DOCTYPE html>
<html lang="en">
<head>
<meta charset="utf-8">
<title>Elder Aid Center – Direct Mail Brochure</title>
<link rel="stylesheet" href="https://fonts.googleapis.com/css2?family=Lato:wght@400;700;900&family=Tinos:wght@400;700&display=swap">
<style>
  :root {
    --navy: #0b2a5b;
    --blue: #0355a3;
    --red: #ec1f27;
    --sky: #a9c4e4;
    --white: #ffffff;
    --paper-grey: #e9eaec;
    --ink: #1d1d1d;
    --stage: #15171b;
  }
  * { box-sizing: border-box; margin: 0; padding: 0; }
  html, body { width: 1200px; height: 848px; overflow: hidden; }
  body {
    background: var(--stage);
    position: relative;
    font-family: "Tinos", "Times New Roman", serif;
  }
  .sheet {
    position: absolute;
    top: 56px;
    width: 520px;
    height: 736px;
    background: var(--white);
    overflow: hidden;
  }
  .sheet--inside { left: 50px; }
  .sheet--cover { left: 630px; }

  .sheet__swoosh { position: absolute; left: 0; top: 0; }

  /* Inside page */
  .programs {
    position: absolute;
    left: 44px;
    right: 40px;
    top: 132px;
    color: var(--ink);
  }
  .program { margin-bottom: 22px; font-size: 15px; line-height: 1.28; }
  .program__title {
    color: var(--red);
    font-weight: 700;
    font-size: 19px;
  }
  .disclaimer { margin-top: 36px; }
  .disclaimer__title {
    color: var(--red);
    font-weight: 700;
    font-size: 19px;
    margin-bottom: 6px;
  }
  .disclaimer p { font-size: 11px; line-height: 1.3; margin-bottom: 6px; }

  .contact-band {
    position: absolute;
    left: 0; right: 0; bottom: 0;
    height: 118px;
    background: var(--navy);
    color: var(--white);
    font-family: "Lato", Arial, sans-serif;
    padding: 22px 44px 0;
  }
  .contact-band__lead { font-size: 17px; font-weight: 700; }
  .contact-band__phone {
    font-size: 46px;
    font-weight: 900;
    letter-spacing: 1px;
    line-height: 1.15;
  }

  /* Cover */
  .cover__photo {
    position: absolute;
    left: 0; top: 0;
    width: 520px; height: 470px;
    background: radial-gradient(ellipse at 70% 45%, #e3d6c8 0%, #c9c3a8 35%, #8f9a72 70%, #6f7d5a 100%);
  }
  .brand {
    position: absolute;
    left: 150px;
    top: 420px;
    display: flex;
    align-items: center;
    gap: 12px;
    font-family: "Lato", Arial, sans-serif;
  }
  .brand__dot {
    width: 30px; height: 30px;
    border-radius: 50%;
    background: var(--red);
  }
  .brand__name {
    color: var(--navy);
    font-weight: 700;
    font-size: 24px;
    letter-spacing: 2px;
    text-transform: uppercase;
    line-height: 1.05;
  }
  .brand__tagline {
    position: absolute;
    left: 150px;
    top: 486px;
    font-family: "Tinos", serif;
    font-size: 12px;
    letter-spacing: 1.5px;
    color: var(--navy);
    text-transform: uppercase;
  }
  .slogan {
    position: absolute;
    left: 60px;
    top: 512px;
    font-family: "Lato", Arial, sans-serif;
    font-weight: 900;
    text-transform: uppercase;
    line-height: 1.02;
  }
  .slogan__line { display: block; font-size: 27px; color: var(--navy); }
  .slogan__line--accent { font-size: 38px; color: var(--red); }
  .mail-area {
    position: absolute;
    left: 150px;
    top: 640px;
    font-size: 15px;
    color: var(--ink);
  }
  .cover__footer {
    position: absolute;
    left: 0; right: 0; bottom: 0;
    height: 40px;
    background: linear-gradient(var(--white), var(--paper-grey));
  }
</style>
</head>
<body>

  <section class="sheet sheet--inside">
    <svg class="sheet__swoosh" width="520" height="130" viewBox="0 0 520 130" aria-hidden="true">
      <path d="M0,38 C160,10 360,20 520,70 L520,78 C360,30 160,22 0,48 Z" fill="var(--sky)"/>
      <path d="M0,56 C170,28 360,40 520,100 L520,116 C360,58 170,48 0,76 Z" fill="var(--red)"/>
      <path d="M0,24 C150,2 360,4 520,46 L520,52 C360,12 150,10 0,32 Z" fill="var(--blue)"/>
      <path d="M0,82 C170,56 360,66 520,124 L520,130 L0,130 Z" fill="#dfe6ef" opacity=".7"/>
    </svg>

    <div class="programs">
      <p class="program"><span class="program__title">Sanorel</span> - over 1 in 5 recieve help from state Sanorel. Sanorel programs for seniors and persons on Vitalcor can pay doctor copays, deductibles, and assist with medical bills.</p>
      <p class="program"><span class="program__title">Silver Bridge Program</span> - receive Federal assistance with prescription medications, deductibles, copays, and drug plan premiums.</p>
      <p class="program"><span class="program__title">Vitalcor Thrift Program</span> - many adults 65 and over are eligible to receive Vitalcor at no cost. The program will pay your Vitalcor Tier K premium and can even refund some previous payments.</p>

      <div class="disclaimer">
        <h2 class="disclaimer__title">Government Disclaimer</h2>
        <p>This nonprofit is not affiliated with any state or federal agency. Eligibility for each program is set by the agency and depends on limited income and assets.</p>
        <p>Our help is free of charge. Final decisions on every application are made by the agency that runs the program.</p>
      </div>
    </div>

    <div class="contact-band">
      <p class="contact-band__lead">To learn more call your local county case manager</p>
      <p class="contact-band__phone">800-555-0142</p>
    </div>
  </section>

  <section class="sheet sheet--cover">
    <div class="cover__photo" role="img" aria-label="Photo of a smiling senior couple embracing outdoors"></div>
    <svg class="sheet__swoosh" width="520" height="736" viewBox="0 0 520 736" aria-hidden="true">
      <path d="M0,250 C150,240 330,320 520,520 L520,560 C330,360 150,290 0,300 Z" fill="var(--blue)"/>
      <path d="M0,300 C150,292 330,370 520,570 L520,600 C330,400 150,320 0,326 Z" fill="var(--red)"/>
      <path d="M0,326 C150,318 330,400 520,600 L520,614 C330,420 150,338 0,342 Z" fill="var(--sky)"/>
      <path d="M0,342 C150,338 330,420 520,614 L520,736 L0,736 Z" fill="var(--white)"/>
    </svg>

    <div class="brand">
      <span class="brand__dot"></span>
      <span class="brand__name">Elder Aid<br>Center</span>
    </div>
    <p class="brand__tagline">Life, Health and Wealth Protection</p>

    <h1 class="slogan">
      <span class="slogan__line">Knowledge is power.</span>
      <span class="slogan__line slogan__line--accent">Lets up help</span>
      <span class="slogan__line">empower you.</span>
    </h1>

    <p class="mail-area">Blank area for address</p>
    <div class="cover__footer"></div>
  </section>

</body>
</html>
```